HiItsJonBrell.com needs a modern, eye-catching business card design

My name is Jon Brell and I own a video training (software development industry) website. I need a business card design that is eye catching for when I travel to conferences or do seminars. I would prefer something simple but bold. Something along the lines of this: https://pixvaultstatic.example/gallery_img/530172/44018/44018_9917302_530172_image.jpg

Note that I do not have a specific logo, but I do have an caricature I use on my site of myself. I've not attached it because I'm not really a fan of having it on my business cards. I would prefer lettering instead of an image. You can go to my website (https://hiitsjonbrell.com) for inspiration.

I want to add the following information on my card (the order of these, their size, and their casing is up to you):

Jon Brell
jon@HiItsJonBrell.com
@HiItsJonBrell
HiItsJonBrell.com
vidsharehub.example/HiItsJonBrell

I would also like to have somewhere on the card a small ad that says "Get a free course at https://HiItsJonBrell.com/FreeCourse". Feel free to play with that wording or layout if you need. I would prefer this text to be at the bottom of the card and subtle. Some small eye-catching thing might be ok but nothing huge or garish.

I plan on printing this card at pressquill.example (https://www.pressquill.example/us/design-guidelines/business-cards.html). I would like it to be the standard size (3.66" x 2.16"). I would prefer rounded corners and horizontal orientation. This is a two-side design. I would prefer the side with all of the information be primarily white but I like color text (again, flexible on that). On the front side, I like simple. Maybe just HiItsJonBrell.com (casing on that is up to you - whatever looks and reads the best - that goes for all of the casing). As for font choices, I prefer a modern, clean font. For example, Open Sans Light can be a nice option.

Website Info (might be helpful for the card):
Color Palette

Darkest blue - #263246
Alternate blue - #2F4E6A
Light blue - #2A98C3
Orange - #FF6201
White - #FFFFFF

Font for Jon Brell Logo

Jellyka Estryas Handwriting
http://www.typecrate.example/jellyka_estryas_handwriting.font

Fonts for Site Content and VidShare Thumbnails

Lovelo (bold title font)
http://www.glyphmill.example/lovelo-font/

Open Sans (body font)
http://www.letterbarn.example/fonts/open-sans

Industry/Entity Type

Software Development

Contact Information for Business Card

Jon Brell
jon@HiItsJonBrell.com
@HiItsJonBrell
HiItsJonBrell.com
vidsharehub.example/HiItsJonBrell

Get a free course at https://HiItsJonBrell.com/FreeCourse

Colors

Designer to choose colors to be used in the design.

Requirements
Nice to have
• Modern color - maybe primarily a color on the front and then that color as an accent on the back.
Should not have
• Lots of colors - I LOVE color but do not want a rainbow of colors on the card.

```html
<!DOCTYPE html>
<html lang="en">
<head>
<meta charset="utf-8">
<title>Jon Brell – Business Cards</title>
<link href="https://fonts.googleapis.com/css2?family=Montserrat:wght@700&family=Open+Sans:wght@300;400;600&display=swap" rel="stylesheet">
<style>
  :root {
    --navy: #263246;
    --navy-alt: #2F4E6A;
    --orange: #FF6201;
    --white: #FFFFFF;
    --backdrop: #ECE8E3;
    --ink-soft: #4A5568;
  }
  * { margin: 0; padding: 0; box-sizing: border-box; }
  html, body { width: 1200px; height: 891px; overflow: hidden; }
  body {
    background: var(--backdrop);
    font-family: "Open Sans", Arial, sans-serif;
    position: relative;
  }
  .card {
    position: absolute;
    width: 560px;
    height: 330px;
    border-radius: 14px;
    overflow: hidden;
    box-shadow: 0 10px 28px rgba(38, 50, 70, 0.22);
  }

  /* ---------- Front side ---------- */
  .card--front { left: 560px; top: 80px; background: var(--navy); }
  .front-brand {
    position: absolute; left: 150px; top: 98px;
    display: flex; align-items: center; gap: 22px;
  }
  .portrait {
    width: 78px; height: 78px; border-radius: 50%;
    background: radial-gradient(circle at 50% 40%, #D9A47E 0%, #8A5E44 55%, #2F4E6A 100%);
  }
  .brand-name {
    color: var(--white);
    font-weight: 300;
    font-size: 40px;
    letter-spacing: 2px;
    line-height: 1;
  }
  .brand-role {
    color: var(--white);
    font-size: 12px;
    margin-top: 12px;
    letter-spacing: 0.3px;
  }
  .front-site {
    position: absolute; left: 0; top: 212px;
    width: 215px; height: 20px;
    background: var(--orange);
    color: var(--navy);
    font-size: 11px; font-weight: 600; letter-spacing: 1px;
    line-height: 20px; padding-left: 26px;
  }
  .front-bars {
    position: absolute; left: 226px; top: 230px;
    width: 9px; height: 20px;
    border-left: 3px solid var(--orange);
    border-right: 3px solid var(--orange);
  }
  .front-offer {
    position: absolute; left: 246px; right: 0; top: 250px;
    height: 20px;
    background: var(--orange);
    color: var(--navy);
    font-size: 11px; font-weight: 600;
    line-height: 20px; text-align: right; padding-right: 22px;
  }

  /* ---------- Info side ---------- */
  .card--info { left: 90px; top: 470px; background: var(--white); }
  .info-header {
    position: absolute; left: 0; top: 0; width: 100%; height: 138px;
    background: var(--navy);
    border-bottom: 4px solid var(--orange);
  }
  .info-header .portrait {
    position: absolute; left: 200px; top: 38px;
    width: 74px; height: 74px;
  }
  .info-header .brand-name {
    position: absolute; left: 292px; top: 52px;
    font-size: 36px;
  }
  .info-name {
    position: absolute; left: 36px; top: 178px;
    font-family: "Montserrat", Arial, sans-serif;
    font-weight: 700;
    font-size: 21px; letter-spacing: 6px;
    color: var(--navy);
  }
  .info-role {
    position: absolute; left: 38px; top: 208px;
    font-size: 11px; color: var(--navy);
  }
  .info-divider {
    position: absolute; left: 262px; top: 172px;
    width: 1.5px; height: 62px; background: var(--navy);
  }
  .contact-list {
    position: absolute; left: 290px; top: 166px;
    list-style: none;
  }
  .contact-list li {
    display: flex; align-items: center; gap: 10px;
    font-size: 12.5px; color: var(--navy);
    margin-bottom: 9px;
  }
  .contact-icon { width: 16px; height: 16px; flex: none; }
  .offer-tab {
    position: absolute; left: 0; bottom: 0;
    width: 300px; height: 58px;
    background: var(--navy);
    clip-path: polygon(0 0, 92% 0, 100% 100%, 0 100%);
    color: var(--white);
    font-size: 11px; line-height: 1.45;
    padding: 12px 0 0 36px;
  }
  .info-footer-line {
    position: absolute; left: 300px; right: 0; bottom: 0;
    height: 4px; background: var(--orange);
  }
</style>
</head>
<body>

  <section class="card card--front" aria-label="Business card front">
    <div class="front-brand">
      <div class="portrait" role="img" aria-label="Caricature portrait of Jon Brell"></div>
      <div>
        <div class="brand-name">Jon Brell</div>
        <div class="brand-role">Software Development</div>
      </div>
    </div>
    <div class="front-site">www.hiitsjonbrell.com</div>
    <div class="front-bars"></div>
    <div class="front-offer">Get a free course at www.hiitsjonbrell.com/FreeCourse</div>
  </section>

  <section class="card card--info" aria-label="Business card contact side">
    <div class="info-header">
      <div class="portrait" role="img" aria-label="Caricature portrait of Jon Brell"></div>
      <div class="brand-name">Jon Brell</div>
    </div>

    <div class="info-name">JON BRELL</div>
    <div class="info-role">Software Development</div>
    <div class="info-divider"></div>

    <ul class="contact-list">
      <li>
        <svg class="contact-icon" viewBox="0 0 16 16"><circle cx="8" cy="8" r="8" fill="#263246"/><circle cx="8" cy="8" r="3" fill="#fff"/></svg>
        vidsharehub.example/HiItsJonBrell
      </li>
      <li>
        <svg class="contact-icon" viewBox="0 0 16 16"><circle cx="8" cy="8" r="8" fill="#263246"/><rect x="4" y="5" width="8" height="6" fill="none" stroke="#fff" stroke-width="1.2"/><path d="M4 5 L8 8.5 L12 5" fill="none" stroke="#fff" stroke-width="1.2"/></svg>
        jon@hiitsjonbrell.com
      </li>
      <li>
        <svg class="contact-icon" viewBox="0 0 16 16"><circle cx="8" cy="8" r="8" fill="#263246"/><rect x="4" y="4.5" width="8" height="5.5" fill="none" stroke="#fff" stroke-width="1.2"/><path d="M6 12 H10" stroke="#fff" stroke-width="1.2"/></svg>
        https://hiitsjonbrell.com
      </li>
    </ul>

    <div class="offer-tab">Get a free course at<br>https://HiItsJonBrell.com/FreeCourse</div>
    <div class="info-footer-line"></div>
  </section>

</body>
</html>
```